Tshirt. Car logo stationary ect for construction company
Kr construction
Peter hosking
No address on business card 0417 862 513
Info@krconstruction.example
need designs for all stationary and letterheads. also need designs for a 2005 k47 talvora silver in color with a canopy. also designs for a large builders trailer. and anything else you guys can think of. thankyou very much
need an editable business card as email is still being made. waiting on domain name
peterhosking peterhosking
You guys are on fire. Anyone keen on doing some designs for my car letterheads ect. Go Fenwick tolgraphix just to name a couple
I have uploaded one wrong designs the square desing is different will upload a new design tonight

```html
<!DOCTYPE html>
<html lang="en">
<head>
<meta charset="utf-8">
<title>Kr construction — Business card</title>
<link href="https://fonts.googleapis.com/css2?family=Montserrat:wght@400;500;600;700&display=swap" rel="stylesheet">
<style>
  :root {
    --page: #e9e6e1;
    --card-white: #ffffff;
    --card-black: #111111;
    --green: #8cc63f;
    --grey: #cfcfcf;
    --ink: #2a2a2a;
    --ink-soft: #6b6b6b;
  }
  html, body {
    margin: 0;
    width: 1200px;
    height: 978px;
    overflow: hidden;
    background: var(--page);
    font-family: "Montserrat", sans-serif;
  }
  .card {
    position: absolute;
    left: 220px;
    width: 760px;
    height: 434px;
    border-radius: 26px;
    overflow: hidden;
    box-shadow: 0 10px 28px rgba(0,0,0,0.18);
  }
  /* Front */
  .card-front {
    top: 40px;
    background: var(--card-white);
  }
  .card-front .edge-band {
    position: absolute;
    left: 0; right: 0; bottom: 0;
    height: 34px;
    background: var(--green);
  }
  .brand {
    position: absolute;
    display: flex;
    align-items: center;
    gap: 12px;
  }
  .brand-mark {
    width: 20px;
    height: 20px;
    border-radius: 50%;
    background: var(--green);
  }
  .brand-name {
    font-weight: 500;
  }
  .tagline {
    position: absolute;
    color: var(--green);
    font-weight: 400;
    letter-spacing: 0.12em;
  }
  .card-front .brand { left: 70px; top: 176px; }
  .card-front .brand-name { font-size: 26px; color: var(--ink-soft); }
  .card-front .tagline { left: 102px; top: 216px; font-size: 13px; }
  .divider {
    position: absolute;
    left: 400px;
    top: 60px;
    width: 2px;
    height: 310px;
    background: var(--ink);
  }
  .contact {
    position: absolute;
    left: 434px;
    top: 74px;
    color: var(--ink);
  }
  .person-name {
    margin: 0;
    font-size: 22px;
    font-weight: 700;
    text-transform: uppercase;
    letter-spacing: 0.06em;
  }
  .person-role {
    margin: 4px 0 44px;
    font-size: 14px;
    color: var(--ink-soft);
  }
  .contact-list {
    list-style: none;
    margin: 0;
    padding: 0;
    font-size: 14px;
  }
  .contact-list li {
    display: flex;
    align-items: center;
    gap: 12px;
    margin-bottom: 14px;
  }
  .contact-list svg { width: 14px; height: 14px; fill: var(--ink); flex: none; }
  /* Back */
  .card-back {
    top: 514px;
    background: var(--card-black);
  }
  .stripe-grey {
    position: absolute;
    left: 0; top: 0; bottom: 0;
    width: 34px;
    background: var(--grey);
  }
  .stripe-green {
    position: absolute;
    left: 34px; top: 0; bottom: 0;
    width: 8px;
    background: var(--green);
  }
  .card-back .brand { left: 196px; top: 180px; }
  .card-back .brand-name { font-size: 38px; color: #ffffff; }
  .card-back .tagline { left: 228px; top: 236px; font-size: 16px; }
</style>
</head>
<body>
  <section class="card card-front" aria-label="Business card front">
    <div class="brand">
      <span class="brand-mark"></span>
      <span class="brand-name">Kr construction</span>
    </div>
    <div class="tagline">Plan Frame Renew</div>
    <div class="divider"></div>
    <div class="contact">
      <p class="person-name">Peter Hosking</p>
      <p class="person-role">Managing Director</p>
      <ul class="contact-list">
        <li>
          <svg viewBox="0 0 24 24"><path d="M6.6 10.8a15.1 15.1 0 0 0 6.6 6.6l2.2-2.2a1 1 0 0 1 1-.25 11.4 11.4 0 0 0 3.6.57 1 1 0 0 1 1 1V20a1 1 0 0 1-1 1A17 17 0 0 1 3 4a1 1 0 0 1 1-1h3.5a1 1 0 0 1 1 1 11.4 11.4 0 0 0 .57 3.6 1 1 0 0 1-.25 1z"/></svg>
          0417 862 513
        </li>
        <li>
          <svg viewBox="0 0 24 24"><path d="M2 5h20v14H2zM4 7v.5l8 5 8-5V7l-8 5z"/></svg>
          Info@krconstruction.example
        </li>
        <li>
          <svg viewBox="0 0 24 24"><circle cx="12" cy="12" r="10" fill="none" stroke="#2a2a2a" stroke-width="2"/><path d="M2 12h20M12 2c3 3 3 17 0 20M12 2c-3 3-3 17 0 20" fill="none" stroke="#2a2a2a" stroke-width="1.5"/></svg>
          www.krconstruction.example
        </li>
      </ul>
    </div>
    <div class="edge-band"></div>
  </section>

  <section class="card card-back" aria-label="Business card back">
    <div class="stripe-grey"></div>
    <div class="stripe-green"></div>
    <div class="brand">
      <span class="brand-mark"></span>
      <span class="brand-name">Kr construction</span>
    </div>
    <div class="tagline">Plan Frame Renew</div>
  </section>
</body>
</html>
```